依頼詳細
PCとスマホデザインの両方納品をいただきますが、
まずはデザインイメージが確認しやすいPCページのみの提案をお願いします。
スマホページは当選者に納品時にお願いしたいと思います。
スマホサイズについて、表示は横幅375pxで作成し、
デザインデータは2倍の横幅750pxのカンバスサイズで作成してください。
(Retinaディスプレイに対応するため)
レスポンシブウェブデザインを意識したデザインでお願いします。

■サイトマップ
添付の画面遷移図をご確認ください。

■参考サイト
http://hoshizora-tetsuko.co.jp/

■内容について
鋳造部品等を製作する会社のサイトリニューアルになります。
既存サイト
http://www.senbeiseiko.com/kiyora/index.html

■素材写真
画像データについては、フリー素材から流用して
イメージ画像に当て込んでください。
足りない場合は、一旦他のサイトの写真をサンプルとして
入れてください。(サンプルなどの表記をお願いします)
また、購入が必要な写真などを利用した場合、
価格とサイト名を教えてください。

また、Lumera Photosで定期契約をしていますので、
Lumera Photosの画像は使用できます。
デザイン時はカンプ画像をお入れいただきますようお願いします。

■ワイヤーフレーム
https://mock.wirevista.net/view/1a2b3c4d-5e6f-4a7b-8c9d-0e1f2a3b4c5d-8812/?fullscreen
コンテンツの構成としてワイヤーフレームを作成しましたが
必ずしもワイヤーフレームの通りではなくて大丈夫です。
TOPページに配置するコンテンツを見ていただき、デザインは
デザイナーの皆様におまかせしたいと思います。

----------------------------------------------------------------------------
【制作物に対するお願い】

■フォントについて
・無料で使えるフォントで作成をお願いします。
・OSに紐づくフォントの使用は控えていただければと思います (ヒラギノなど)

ページ数
1ページ
希望イメージ
シンプル 複雑
単色 カラフル
暗い 明るい
日常 高級
遊び心 厳粛
未来的 伝統的
女性的 男性的
希望する色
アクセントカラー:茶色、もしくは青色
納品ファイル
• 高解像度JPG (.jpg)
• イラストレーター形式 (.ai)
• フォトショップ形式 (.psd)
補足説明
上記のいずれか1つ(アウトラインありとなしの2つ)と高解像度JPGを納品お願いします。
adobe XDでの納品も可能です。

```html
<!DOCTYPE html>
<html lang="ja">
<head>
<meta charset="utf-8">
<title>星川伸銅株式会社</title>
<link rel="stylesheet" href="https://fonts.googleapis.com/css2?family=Cormorant+Garamond:wght@500;600&family=Noto+Serif+JP:wght@400;500;600;700&display=swap">
<style>
:root{
  --maroon:#7a2328;
  --maroon-dark:#5c191d;
  --maroon-deep:#4a1317;
  --ink:#2a2a2a;
  --paper:#ffffff;
  --grey:#e7e7e7;
  --muted:#8a6a6a;
}
*{margin:0;padding:0;box-sizing:border-box}
html,body{width:1200px;height:4988px;overflow:hidden}
body{font-family:"Noto Serif JP",serif;color:var(--ink);background:var(--paper);position:relative}
.en{font-family:"Cormorant Garamond",serif;font-weight:600;letter-spacing:.18em}
a{color:inherit;text-decoration:none}

/* header */
.site-header{position:absolute;top:0;left:0;width:1200px;height:60px;background:#fff;display:flex;align-items:center;z-index:2}
.site-header .brand{margin-left:22px;font-size:15px;font-weight:600;letter-spacing:.08em}
.global-nav{margin-left:auto;display:flex;gap:0;height:60px;align-items:center}
.global-nav a{font-size:13px;letter-spacing:.1em;padding:0 32px;border-left:1px solid #ccc;line-height:14px}
.header-contact{width:270px;height:60px;background:var(--maroon);color:#fff;display:flex;align-items:center;justify-content:center;font-size:13px;letter-spacing:.12em;margin-left:20px}

/* hero */
.hero{position:absolute;top:60px;left:0;width:1200px;height:740px;background:linear-gradient(180deg,#2a231f 0%,#5a3a24 35%,#8a5a2c 55%,#3b2a22 80%,#1e1a18 100%)}
.hero-copy{position:absolute;left:22px;top:590px;color:#fff;font-size:34px;font-weight:600;letter-spacing:.12em;text-shadow:0 2px 8px rgba(0,0,0,.5)}

/* about */
.about{position:absolute;top:800px;left:0;width:1200px;height:550px}
.about-panel{position:absolute;left:0;top:0;width:600px;height:520px;background:var(--maroon);color:#fff;padding:40px 0 0 70px}
.about-photo{position:absolute;left:600px;top:0;width:600px;height:550px;background:radial-gradient(circle at 40% 50%,#ffd88a 0%,#e08a2a 18%,#6a4a36 45%,#2b2c33 100%)}
.sec-title{font-size:44px;font-weight:500;letter-spacing:.14em;line-height:1}
.sec-sub{font-size:13px;letter-spacing:.2em;margin-top:12px}
.about-lead{font-size:18px;line-height:1.8;margin-top:44px;letter-spacing:.08em}
.about-body{font-size:13px;line-height:2.1;margin-top:28px;width:460px;letter-spacing:.05em}
.btn-line{display:flex;align-items:center;width:200px;height:50px;background:var(--maroon-deep);color:#fff;font-size:12px;letter-spacing:.2em;padding-left:28px;position:relative}
.btn-line::after{content:"";position:absolute;right:-60px;top:25px;width:140px;height:1px;background:#fff}
.about .btn-line{margin-top:38px}

/* product */
.product{position:absolute;top:1350px;left:0;width:1200px;height:870px}
.centered-head{text-align:center;color:var(--maroon)}
.product .centered-head{padding-top:110px}
.centered-head .sec-sub{color:#555;margin-top:8px}
.product-grid{position:absolute;top:250px;left:0;width:1200px;height:620px;display:flex}
.product-card{width:400px;height:620px;position:relative;color:#fff}
.product-card .shade{position:absolute;left:0;right:0;bottom:0;height:170px;background:linear-gradient(180deg,rgba(20,20,20,0) 0%,rgba(20,20,20,.75) 40%)}
.product-card h3{position:absolute;left:24px;top:452px;font-size:19px;font-weight:600;letter-spacing:.12em;width:350px;padding-bottom:10px;border-bottom:1px solid rgba(255,255,255,.6)}
.product-card p{position:absolute;left:24px;top:502px;width:350px;font-size:12px;line-height:1.9}
.photo-machine{background:linear-gradient(135deg,#3b3f48,#7a3a2a 45%,#2e3440)}
.photo-electric{background:linear-gradient(180deg,#3f7fc8 0%,#8ab4e0 45%,#5a5e66 80%,#2e3036 100%)}
.photo-parts{background:radial-gradient(circle at 50% 40%,#d6d6d6,#8a8a8a 45%,#3a3a3a 100%)}

/* guidance */
.guidance{position:absolute;top:2220px;left:0;width:1200px;height:540px}
.guidance-photo{position:absolute;left:0;top:0;width:600px;height:540px;background:linear-gradient(160deg,#3a2c25 0%,#8a5a30 40%,#c07a3a 55%,#3a2a22 100%)}
.slider-dots{position:absolute;left:285px;top:506px;display:flex;gap:8px}
.slider-dots span{width:8px;height:8px;border-radius:50%;background:rgba(255,255,255,.5)}
.slider-dots span.on{background:#fff}
.guidance-panel{position:absolute;left:600px;top:30px;width:600px;height:510px;background:var(--maroon);color:#fff;padding:40px 0 0 50px}
.guidance-panel .sec-title{font-size:40px;border-bottom:1px solid rgba(255,255,255,.6);padding-bottom:8px;width:520px}
.guidance-lead{font-size:18px;line-height:1.8;margin-top:52px;letter-spacing:.08em}
.guidance-body{font-size:13px;line-height:2.1;margin-top:22px;width:480px}
.guidance .btn-line{margin-top:44px}

/* recruit */
.recruit{position:absolute;top:2840px;left:0;width:1200px;height:400px;background:linear-gradient(90deg,#1d2a3a 0%,#2e3a4a 40%,#3a3640 60%,#5a3a2a 100%);color:#fff;text-align:center}
.recruit::before{content:"";position:absolute;inset:0;background:rgba(0,0,0,.35)}
.recruit-inner{position:relative;padding-top:48px}
.recruit .sec-title{font-size:40px}
.recruit .sec-sub{margin-top:6px}
.recruit-lead{font-size:20px;font-weight:600;letter-spacing:.12em;margin-top:30px}
.recruit-body{font-size:13px;line-height:2;margin-top:18px}
.btn-fill{display:inline-flex;align-items:center;justify-content:center;width:240px;height:52px;background:var(--maroon);color:#fff;font-size:12px;letter-spacing:.14em}
.recruit .btn-fill{margin-top:26px}

/* news */
.news{position:absolute;top:3240px;left:0;width:1200px;height:840px}
.news .centered-head{padding-top:230px}
.news .centered-head .sec-title{font-size:44px}
.news-list{position:absolute;top:380px;left:70px;display:flex;gap:64px}
.news-item{width:310px}
.news-thumb{width:310px;height:180px}
.thumb-weld{background:linear-gradient(135deg,#1e3a6a,#4a7ac0 50%,#e0a040 80%)}
.thumb-spark{background:radial-gradient(circle at 60% 50%,#f0a040,#7a3a1a 45%,#1e1a1a 100%)}
.thumb-worker{background:linear-gradient(160deg,#6a6a6a,#3a3e44 50%,#a0401a 100%)}
.news-date{font-size:11px;margin-top:14px;letter-spacing:.08em;color:#555}
.news-text{font-size:12px;line-height:1.8;margin-top:4px}
.news .btn-fill{position:absolute;left:480px;top:710px;height:50px}

/* contact */
.contact{position:absolute;top:4080px;left:0;width:1200px;height:520px;background:var(--grey);text-align:center}
.contact .centered-head{padding-top:70px}
.contact .sec-title{color:#c9a39f}
.contact-lead{font-size:14px;margin-top:14px;letter-spacing:.08em}
.contact-tel{font-size:30px;margin-top:44px;letter-spacing:.1em}
.contact-tel small{font-size:18px;margin-right:6px}
.contact-hours{font-size:11px;margin-top:4px}
.contact .btn-fill{width:420px;height:50px;margin-top:28px}

/* footer */
.site-footer{position:absolute;top:4600px;left:0;width:1200px;height:388px;background:var(--maroon);color:#fff;text-align:center}
.to-top{position:absolute;left:520px;top:-60px;width:160px;height:60px}
.to-top span{position:absolute;left:0;right:0;top:36px;font-size:10px;letter-spacing:.2em;color:#fff}
.footer-name{font-size:22px;font-weight:600;letter-spacing:.12em;padding-top:90px}
.footer-nav{display:flex;justify-content:center;gap:56px;margin-top:40px;font-size:13px;letter-spacing:.1em}
.footer-bar{position:absolute;left:0;bottom:0;width:1200px;height:80px;background:var(--maroon-dark);display:flex;align-items:center;padding:0 70px;font-size:12px}
.footer-bar nav{display:flex;gap:40px}
.footer-bar small{margin-left:auto;font-size:11px;letter-spacing:.05em}
</style>
</head>
<body>

<header class="site-header">
  <div class="brand">星川伸銅株式会社</div>
  <nav class="global-nav">
    <a href="#">会社案内</a><a href="#">製品案内</a><a href="#">製品紹介</a><a href="#">採用情報</a>
  </nav>
  <a class="header-contact" href="#">お問い合わせ</a>
</header>

<section class="hero" role="img" aria-label="鍛造工場の内部、炉の光に照らされた作業場">
  <p class="hero-copy">鍛造技術に、自負と誇りをもって。</p>
</section>

<section class="about">
  <div class="about-panel">
    <h2 class="sec-title en">ABOUT US</h2>
    <p class="sec-sub">星川伸銅とは</p>
    <p class="about-lead">ものづくりのプロとして、<br>確かな技術でお答えします。</p>
    <p class="about-body">星川伸銅株式会社は創業以来、銅合金の鍛造部品を中心に製造を続けてまいりました。確かな品質と技術で、お客様の多様なご要望にお応えします。小ロットから量産まで一貫して対応いたします。</p>
    <a class="btn-line en" href="#">READ MORE</a>
  </div>
  <div class="about-photo" role="img" aria-label="火花を散らしながら金属を加工する様子"></div>
</section>

<section class="product">
  <div class="centered-head">
    <h2 class="sec-title en">PRODUCT</h2>
    <p class="sec-sub">製品紹介</p>
  </div>
  <div class="product-grid">
    <article class="product-card photo-machine" role="img" aria-label="機械部品の配線と部品群">
      <div class="shade"></div>
      <h3>機械部品</h3>
      <p>テキストが入ります。テキストが入ります。テキストが入ります。テキストが入ります。</p>
    </article>
    <article class="product-card photo-electric" role="img" aria-label="青空の下の電気設備と碍子">
      <div class="shade"></div>
      <h3>電気製品</h3>
      <p>テキストが入ります。テキストが入ります。テキストが入ります。テキストが入ります。</p>
    </article>
    <article class="product-card photo-parts" role="img" aria-label="金属製の歯車部品が並ぶ様子">
      <div class="shade"></div>
      <h3>その他部品</h3>
      <p>テキストが入ります。テキストが入ります。テキストが入ります。テキストが入ります。</p>
    </article>
  </div>
</section>

<section class="guidance">
  <div class="guidance-photo" role="img" aria-label="溶けた金属を扱う鋳造現場">
    <div class="slider-dots"><span class="on"></span><span></span><span></span></div>
  </div>
  <div class="guidance-panel">
    <h2 class="sec-title en">GUIDANCE</h2>
    <p class="sec-sub">製品案内</p>
    <p class="guidance-lead">充実した設備と確かな技術で<br>お客様のご要望に応えます。</p>
    <p class="guidance-body">星川伸銅株式会社は、自動化ラインや各種検査設備を備え、一貫した体制で製品をお届けしています。お客様のご要望に合わせた最適なご提案をいたします。</p>
    <a class="btn-line en" href="#">READ MORE</a>
  </div>
</section>

<section class="recruit" role="img" aria-label="工場で働く人の作業風景と火花">
  <div class="recruit-inner">
    <h2 class="sec-title en">RECRUIT</h2>
    <p class="sec-sub">採用情報</p>
    <p class="recruit-lead">星川伸銅でともに働く仲間を募集しています。</p>
    <p class="recruit-body">星川伸銅株式会社では、鍛造部品の製造に携わる、意欲ある仲間を募集しています。<br>未経験の方も歓迎です。ものづくりに興味のある方のご応募をお待ちしております。</p>
    <a class="btn-fill" href="#">エントリーはこちら</a>
  </div>
</section>

<section class="news">
  <div class="centered-head">
    <h2 class="sec-title en">NEWS</h2>
    <p class="sec-sub">お知らせ</p>
  </div>
  <div class="news-list">
    <article class="news-item">
      <div class="news-thumb thumb-weld" role="img" aria-label="溶接作業の様子"></div>
      <p class="news-date">2021.10.10</p>
      <p class="news-text">テキストが入ります。テキストが入ります。テキストが入ります。</p>
    </article>
    <article class="news-item">
      <div class="news-thumb thumb-spark" role="img" aria-label="研削で火花が飛ぶ様子"></div>
      <p class="news-date">2021.10.10</p>
      <p class="news-text">テキストが入ります。テキストが入ります。テキストが入ります。</p>
    </article>
    <article class="news-item">
      <div class="news-thumb thumb-worker" role="img" aria-label="工場内で作業する様子"></div>
      <p class="news-date">2021.10.10</p>
      <p class="news-text">テキストが入ります。テキストが入ります。テキストが入ります。</p>
    </article>
  </div>
  <a class="btn-fill" href="#">一覧を見る</a>
</section>

<section class="contact">
  <div class="centered-head">
    <h2 class="sec-title en">CONTACT</h2>
    <p class="sec-sub">お問い合わせ</p>
  </div>
  <p class="contact-lead">ご質問やご相談を承ります。どうぞ、お気軽にお問い合わせください。</p>
  <p class="contact-tel"><small>TEL</small>0256-00-4187</p>
  <p class="contact-hours">受付時間 9:00〜17:00（土日祝除く）</p>
  <a class="btn-fill" href="#">お問い合わせフォームはこちら</a>
</section>

<footer class="site-footer">
  <a class="to-top" href="#">
    <svg width="160" height="60" viewBox="0 0 160 60" aria-hidden="true"><polygon points="0,60 80,0 160,60" fill="#7a2328"/></svg>
    <span class="en">TOP</span>
  </a>
  <p class="footer-name">星川伸銅株式会社</p>
  <nav class="footer-nav">
    <a href="#">会社案内</a><a href="#">製品紹介</a><a href="#">製品案内</a><a href="#">採用情報</a>
  </nav>
  <div class="footer-bar">
    <nav><a href="#">個人情報</a><a href="#">プライバシーポリシー</a><a href="#">サイトマップ</a></nav>
    <small>Hoshikawa Shindo Co., LTD. All Rights Reserved.</small>
  </div>
</footer>

</body>
</html>
```